Broschüre für Planungen und Verkauf von Häusern
Zielgruppe
Planungen und Verkauf von Häusern
Aufgabenstellung
Es sollte auf der Basis meines erstellten Logo und den Farben basieren. auf der vorderen Seite das Logo mit Firmennamen und
ein Spruch
Ein guter Plan heute, ist besser als ein perfekter Plan morgen
Innen aufklappbar mit zwei Laschen zum Einlegen von Angeboten usw. sowie einen Schlitz zum Einbringen von Visitenkarten
Rückseite Firmennamen Adressen Telefon usw.
Ein Beisdspiel lege ich bei, nur sollten die Farben angepasst werden

```html
<!DOCTYPE html>
<html lang="de">
<head>
<meta charset="utf-8">
<title>Falkenried Bau GmbH – Mappe</title>
<link href="https://fonts.googleapis.com/css2?family=Montserrat:ital,wght@0,400;0,500;0,600;0,700;1,700&display=swap" rel="stylesheet">
<style>
  :root {
    --backdrop: #8a8584;
    --brand-blue: #1557a8;
    --brand-orange: #f9ab3b;
    --paper: #ffffff;
    --text-grey: #6d6e72;
    --photo-sky: #5d7384;
    --photo-ground: #3c4a46;
  }
  * { box-sizing: border-box; margin: 0; padding: 0; }
  html, body { width: 715px; height: 1200px; overflow: hidden; }
  body {
    background: var(--backdrop);
    font-family: "Montserrat", sans-serif;
    position: relative;
  }
  .sheet { position: absolute; left: 27px; top: 194px; width: 660px; height: 812px; }

  /* Outer spread */
  .outer-spread { position: absolute; left: 0; top: 0; width: 660px; height: 341px; display: flex; }
  .back-panel {
    position: relative; width: 330px; height: 341px;
    background: linear-gradient(180deg, var(--photo-sky) 0%, #566775 45%, #4c5457 75%, var(--photo-ground) 100%);
  }
  .back-panel .contact-block { position: absolute; left: 37px; top: 164px; color: #fff; font-size: 9px; font-weight: 500; }
  .contact-company { margin-bottom: 16px; font-size: 9.5px; }
  .contact-row { display: flex; align-items: center; gap: 5px; height: 14px; margin-bottom: 16px; }
  .contact-row svg { width: 11px; height: 11px; flex: none; }
  .back-brand {
    position: absolute; left: 218px; top: 272px;
    color: var(--brand-orange); font-weight: 500; font-size: 10px;
  }

  .cover-panel { position: relative; width: 330px; height: 341px; background: var(--paper); overflow: hidden; }
  .cover-brand {
    position: absolute; top: 106px; left: 0; width: 100%; text-align: center;
    color: var(--brand-blue); font-weight: 500; font-size: 20px;
  }
  .cover-claim { position: absolute; top: 214px; left: 0; width: 100%; text-align: center; }
  .claim-line { font-weight: 700; font-size: 13px; line-height: 24px; }
  .claim-blue { color: var(--brand-blue); font-variant: small-caps; }
  .claim-blue .plain-word { font-variant: normal; }
  .claim-orange { color: var(--brand-orange); font-style: italic; }
  .cover-swoosh { position: absolute; left: 0; bottom: 0; width: 330px; height: 80px; }

  /* Inner spread */
  .inner-spread { position: absolute; left: 0; top: 363px; width: 660px; height: 330px; background: var(--paper); overflow: hidden; }
  .inner-intro {
    position: absolute; left: 29px; top: 28px; z-index: 1;
    color: var(--text-grey); font-size: 10.5px; font-weight: 500; line-height: 13px;
  }
  .inner-drawing {
    position: absolute; left: 140px; top: 0; width: 520px; height: 330px;
    background: linear-gradient(135deg, #ffffff 0%, #f4f4f5 40%, #ececee 100%);
    clip-path: polygon(19% 0, 30% 0, 100% 85%, 100% 100%, 0 100%);
  }

  /* Pockets */
  .pocket { position: absolute; top: 738px; width: 219px; height: 74px; }
  .pocket-left { left: 0; }
  .pocket-right { left: 441px; }
  .pocket svg { display: block; width: 100%; height: 100%; }
  .pocket-brand {
    position: absolute; left: 12px; top: 17px;
    color: #fff; font-weight: 500; font-size: 6px;
  }
</style>
</head>
<body>
<main class="sheet">

  <section class="outer-spread">
    <div class="back-panel" role="img" aria-label="Foto eines modernen Mehrfamilienhauses mit Holzfassade unter Abendhimmel">
      <div class="contact-block">
        <p class="contact-company">Falkenried Bau GmbH</p>
        <p class="contact-row">
          <svg viewBox="0 0 12 12"><path d="M6 0.5a3.8 3.8 0 0 0-3.8 3.8C2.2 7.2 6 11.5 6 11.5s3.8-4.3 3.8-7.2A3.8 3.8 0 0 0 6 0.5z" fill="#f9ab3b"/><circle cx="6" cy="4.3" r="1.4" fill="#fff"/></svg>
          Lindenallee 42, 10115 Berlin
        </p>
        <p class="contact-row">
          <svg viewBox="0 0 12 12"><path d="M2.5 1.2l2 .3.8 2.3-1.3 1a6 6 0 0 0 3.2 3.2l1-1.3 2.3.8.3 2c-.2.8-1 1.2-1.8 1.1A9 9 0 0 1 1.3 3c-.1-.8.4-1.6 1.2-1.8z" fill="#f9ab3b"/></svg>
          0170- 555 12 34
        </p>
        <p class="contact-row">
          <svg viewBox="0 0 12 12"><circle cx="6" cy="6" r="5.5" fill="#f9ab3b"/><circle cx="6" cy="6" r="3.4" fill="none" stroke="#fff" stroke-width=".7"/><path d="M2.6 6h6.8M6 2.6v6.8" stroke="#fff" stroke-width=".7"/></svg>
        </p>
        <p class="contact-row">
          <svg viewBox="0 0 12 12"><circle cx="6" cy="6" r="5.5" fill="#f9ab3b"/><circle cx="6" cy="6" r="1.7" fill="none" stroke="#fff" stroke-width=".8"/><path d="M7.7 6v.8c0 .9 1.4.9 1.4-.4A3.2 3.2 0 1 0 7.6 9" fill="none" stroke="#fff" stroke-width=".8"/></svg>
          torstenka@postfeld.de
        </p>
      </div>
      <p class="back-brand">Falkenried Bau</p>
    </div>

    <div class="cover-panel">
      <h1 class="cover-brand">Falkenried Bau GmbH</h1>
      <div class="cover-claim">
        <p class="claim-line claim-blue">Ein guter Plan <span class="plain-word">heute</span></p>
        <p class="claim-line claim-orange">IST BESSER ALS</p>
        <p class="claim-line claim-blue">Ein perfekter Plan morgen</p>
      </div>
      <svg class="cover-swoosh" viewBox="0 0 330 80" preserveAspectRatio="none" aria-hidden="true">
        <path d="M0 66 C120 82 250 80 330 12" fill="none" stroke="#1557a8" stroke-width="1.2"/>
        <path d="M150 78 C240 76 295 50 330 18" fill="none" stroke="#f9ab3b" stroke-width="1.6"/>
      </svg>
    </div>
  </section>

  <section class="inner-spread">
    <p class="inner-intro">Falkenried Bau GmbH – Ihr Partner für<br>Hausplanung und Immobilienverkauf</p>
    <div class="inner-drawing" role="img" aria-label="Feine Linienzeichnung eines modernen Gebäudes mit steilem Dach"></div>
  </section>

  <div class="pocket pocket-left">
    <svg viewBox="0 0 219 74" preserveAspectRatio="none" aria-hidden="true">
      <path d="M0 0 C90 2 170 14 219 40 L219 74 L0 74 Z" fill="#1557a8"/>
    </svg>
    <p class="pocket-brand">Falkenried Bau</p>
  </div>

  <div class="pocket pocket-right">
    <svg viewBox="0 0 219 74" preserveAspectRatio="none" aria-hidden="true">
      <path d="M0 32 C50 12 130 2 219 0 L219 74 L0 74 Z" fill="#f9ab3b"/>
      <path d="M0 40 C50 20 140 6 219 4 L219 74 L0 74 Z" fill="#1557a8"/>
      <path d="M203 10 L216 19" stroke="#f9ab3b" stroke-width="2.2"/>
      <path d="M4 59 L17 68" stroke="#f9ab3b" stroke-width="2.2"/>
    </svg>
  </div>

</main>
</body>
</html>
```